Neon Lodging Offers Website looking for new design

We are a online travel discounter based around hotel accommodations in Las Vegas. We need a wordpress design that will be used as our corporate cover page, and also for the affiliate pages. The current design can be viewed at http://postweaveforum.com/clients/neonoffer/ and the final design needs to include most of the navigation components. The affiliate pages will need a space to display the booking engine, for example, as shown at http://www.qrv.travel/marcoti. Our general color scheme is red/black, and the two logos we use are attached.

Because this is a crowded niche it is extremely important that we set ourselves apart in the design. The more visually stunning and out of the box the design, the better. The site needs to look distinctively different than anything else online. Since the overall layout is very basic and does not have to provide a lot of information, it leaves a lot of flexibility in design concepts.

We realize it is a truncated timetable, which is why the increased fee for your time and guaranteed payout.

Industry/Entity Type

Travel

```html
<!DOCTYPE html>
<html lang="en">
<head>
<meta charset="utf-8">
<title>Neon Lodging Offers</title>
<link href="https://fonts.googleapis.com/css2?family=Open+Sans:wght@300;400;600;700;800&display=swap" rel="stylesheet">
<style>
:root{
  --red:#d01f2e;
  --red-dark:#b3161f;
  --ink:#222222;
  --tile:#4a4a4a;
  --footer:#262626;
  --bar:#6b6b6b;
  --muted:#777777;
  --line:#e2e2e2;
  --yellow:#f6e600;
  --blue-link:#2a86c8;
  --field:#4a4e52;
  --orange:#f59a0c;
}
*{box-sizing:border-box;margin:0;padding:0}
html,body{width:1200px;height:2510px;overflow:hidden}
body{position:relative;background:#fff;font-family:"Open Sans",Arial,sans-serif;color:var(--ink)}
.abs{position:absolute}

/* header */
.site-header{left:0;top:0;width:1200px;height:114px;border-top:4px solid var(--red);border-bottom:4px solid var(--red);background:#fff}
.brand{left:100px;top:34px;display:flex;align-items:center;gap:10px}
.brand-dot{width:30px;height:30px;border-radius:50%;background:var(--red)}
.brand-name{font-size:17px;font-weight:600;color:var(--red)}
.main-nav{left:420px;top:54px;display:flex;align-items:stretch;height:40px}
.main-nav a{display:block;padding:0 22px;font-size:12px;line-height:14px;color:#333;text-decoration:none;border-right:1px dotted #555}
.main-nav a.active{color:var(--red)}
.search-icon{left:1054px;top:58px}

/* hero */
.hero{left:0;top:114px;width:1200px;height:552px;background:linear-gradient(180deg,#5b87b8 0%,#9bb7d3 30%,#c9d6df 50%,#6a5542 70%,#3b2c22 100%)}
.hero-caption{left:375px;top:90px;width:450px;height:245px;background:rgba(80,80,80,.72);text-align:center;color:#fff}
.hero-kicker{font-size:37px;font-weight:300;margin-top:20px;letter-spacing:.5px}
.hero-title{font-size:88px;font-weight:300;line-height:90px;letter-spacing:1px}
.hero-from{font-size:20px;margin-top:2px}
.hero-price{font-size:44px;color:var(--yellow);line-height:46px}
.hero-arrow{top:250px;width:42px;height:42px;border-radius:50%;border:2px solid var(--red);background:rgba(255,255,255,.85);display:flex;align-items:center;justify-content:center}
.hero-arrow.prev{left:18px;border-color:rgba(255,255,255,.6);background:rgba(255,255,255,.2)}
.hero-arrow.next{left:1137px}

/* service tiles */
.service{top:720px;width:322px;height:192px;background:var(--tile);border:4px solid #ececec;box-shadow:0 2px 6px rgba(0,0,0,.35);text-align:center;color:#fff}
.service svg{margin-top:26px}
.service-label{position:absolute;left:0;right:0;top:138px;font-size:23px;font-weight:400}

/* welcome band */
.welcome{left:0;top:969px;width:1200px;height:384px;background:linear-gradient(180deg,#1f3f6e 0%,#2d5e92 45%,#3f89a7 70%,#5fb2bd 85%,#cfd9d3 100%);color:#fff;text-align:center}
.welcome h2{position:absolute;left:0;right:0;top:90px;font-size:33px;font-weight:400}
.welcome h2 b{font-weight:600}
.welcome .quote{position:absolute;left:0;right:0;top:146px;font-size:21px;font-style:italic}
.welcome p{position:absolute;left:150px;right:150px;top:196px;font-size:12.5px;font-weight:600;line-height:21px}
.btn-outline{position:absolute;left:548px;top:297px;width:113px;height:38px;border:2px solid #fff;font-size:12px;line-height:34px;color:#fff}

/* news */
.section-title{left:0;width:1200px;top:1400px;text-align:center;font-size:44px;font-weight:300;letter-spacing:1px}
.section-title b{font-weight:800}
.news-card{top:1476px;width:320px;height:307px;border:1px solid var(--line);background:#fff;box-shadow:0 1px 3px rgba(0,0,0,.15)}
.news-photo{height:184px}
.news-date{font-size:25px;margin:14px 0 0 12px;color:#333}
.news-text{font-size:13.5px;line-height:18px;color:var(--muted);margin:4px 12px 0}
.btn-more{position:absolute;left:106px;bottom:-14px;width:104px;height:28px;border-radius:14px;background:var(--red-dark);color:#fff;font-size:12px;font-weight:700;text-align:center;line-height:28px}

.divider{left:0;top:1841px;width:1200px;height:2px;background:#e9a4a9}

/* deals */
.deals-head{left:100px;top:1895px;width:240px}
.deals-head h3{font-size:27px;font-weight:400;color:var(--red)}
.deals-head p{font-size:11.5px;line-height:17px;color:var(--muted);margin-top:6px}
.deal{top:1887px;width:223px;height:197px;background:#fff;box-shadow:0 1px 4px rgba(0,0,0,.2)}
.deal-photo{height:155px}
.deal-name{font-size:11.5px;font-weight:700;color:var(--red);margin:10px 0 0 14px}
.deal-sub{font-size:10px;color:var(--blue-link);margin:1px 0 0 14px}
.deal-nav{top:1938px;width:28px;height:48px;background:rgba(40,40,40,.75);display:flex;align-items:center;justify-content:center}

/* footer */
.site-footer{left:0;top:2124px;width:1200px;height:333px;background:var(--footer)}
.foot-title{font-size:14px;font-weight:700;color:var(--red)}
.social{display:flex;gap:8px;margin-top:10px}
.social span{width:33px;height:33px;border-radius:50%;border:2px solid #fff}
.avatar{left:385px;top:2156px;width:127px;height:127px;border-radius:50%;background:linear-gradient(160deg,#c9a58c,#8c6a55);border:3px solid #ddd}
.testimonial{left:537px;top:2164px;width:288px}
.testimonial p{font-size:12.5px;line-height:18px;color:#fff;margin-top:6px}
.testimonial .by{font-style:italic;font-size:11.5px;margin-top:12px}
.newsletter{left:870px;top:2164px;width:232px}
.field{height:28px;background:var(--field);margin-top:10px;font-size:11px;color:#aab;line-height:28px;padding-left:10px;display:flex}
.field .go{margin-left:auto;width:30px;background:var(--orange);display:flex;align-items:center;justify-content:center}
.support{left:870px;top:2330px;width:232px;border-top:1px solid #666;padding-top:14px}
.support h4{font-size:17px;font-weight:600;color:var(--red)}
.support .phone{font-size:23px;color:var(--blue-link);line-height:30px}

.bottom-bar{left:0;top:2457px;width:1200px;height:53px;background:var(--bar);color:#fff;font-size:11px}
.bottom-bar .copy{position:absolute;left:100px;top:20px}
.foot-nav{position:absolute;left:336px;top:20px;display:flex}
.foot-nav a{color:#fff;text-decoration:none;padding:0 16px;border-right:1px solid #aaa;font-size:11.5px}
.foot-nav a:last-child{border-right:none}
</style>
</head>
<body>

<header class="site-header abs">
  <div class="brand abs"><span class="brand-dot"></span><span class="brand-name">neonoffers.travel</span></div>
  <nav class="main-nav abs">
    <a class="active" href="#">Holidays &amp;<br>Destinations</a>
    <a href="#">Book<br>Online Now</a>
    <a href="#">Business<br>Travel</a>
    <a href="#">Inbound<br>Exolore UAE</a>
    <a href="#">Travel<br>Essentials &amp; Rewards</a>
  </nav>
  <svg class="search-icon abs" width="30" height="30" viewBox="0 0 30 30"><circle cx="12" cy="12" r="8" fill="none" stroke="#222" stroke-width="2.5"/><line x1="18" y1="18" x2="27" y2="27" stroke="#222" stroke-width="3"/></svg>
</header>

<section class="hero abs" role="img" aria-label="Looking up at a tall iron lattice tower against a cloudy blue sky">
  <div class="hero-caption abs">
    <div class="hero-kicker">5 DAY LAND TOURS</div>
    <div class="hero-title">FRANCE</div>
    <div class="hero-from">From</div>
    <div class="hero-price">$999</div>
  </div>
  <div class="hero-arrow prev abs"><svg width="14" height="14" viewBox="0 0 14 14"><path d="M9 2 L4 7 L9 12" fill="none" stroke="#fff" stroke-width="2"/></svg></div>
  <div class="hero-arrow next abs"><svg width="14" height="14" viewBox="0 0 14 14"><path d="M5 2 L10 7 L5 12" fill="none" stroke="#d01f2e" stroke-width="2.2"/></svg></div>
</section>

<div class="service abs" style="left:100px">
  <svg width="120" height="80" viewBox="0 0 120 80" fill="#d01f2e">
    <circle cx="30" cy="16" r="10"/><circle cx="60" cy="12" r="11"/><circle cx="90" cy="16" r="10"/>
    <rect x="16" y="30" width="28" height="34" rx="4"/><rect x="44" y="26" width="32" height="48" rx="4"/><rect x="76" y="30" width="28" height="34" rx="4"/>
  </svg>
  <div class="service-label">CORPORATE</div>
</div>
<div class="service abs" style="left:440px">
  <svg width="80" height="84" viewBox="0 0 80 84" fill="none" stroke="#fff" stroke-width="6" stroke-linecap="round">
    <circle cx="40" cy="12" r="7" fill="#fff" stroke="none"/>
    <path d="M14 10 L36 30 L58 8"/><path d="M36 30 L38 52 L30 78"/><path d="M38 52 L48 78"/>
  </svg>
  <div class="service-label">LEISURE</div>
</div>
<div class="service abs" style="left:782px">
  <svg width="84" height="84" viewBox="0 0 84 84" fill="none" stroke="#fff" stroke-width="3" stroke-linejoin="round">
    <path d="M6 6 L30 30 M30 12 L30 30 L12 30"/><path d="M78 6 L54 30 M54 12 L54 30 L72 30"/>
    <path d="M6 78 L30 54 M30 72 L30 54 L12 54"/><path d="M78 78 L54 54 M54 72 L54 54 L72 54"/>
  </svg>
  <div class="service-label">INBOUND</div>
</div>

<section class="welcome abs" role="img" aria-label="Turquoise sea and island shoreline with a traveller in a sun hat">
  <h2>Welcome to <b>NeonOffers.travel</b></h2>
  <div class="quote">“ Happy Customers Tell Great Stories ”</div>
  <p>One thing we never expect when traveling is smooth sailing, but that is exactly what we got! The team of travel coordinators made sure every place we went was accessible and if something wasn't right, they always had a back-up plan. What an amazing vacation!</p>
  <div class="btn-outline">Read More</div>
</section>

<h2 class="section-title abs">OUR <b>NEWS</b></h2>

<article class="news-card abs" style="left:100px">
  <div class="news-photo" role="img" aria-label="White caravan parked on green grass" style="background:linear-gradient(180deg,#3e7a33,#d9dde0 40%,#e8eaec 70%,#4f8a38)"></div>
  <div class="news-date">17 Jan 2014</div>
  <p class="news-text">Ut wisi enim ad minim veniam, quis nostrud exerci tation ullamcorper suscipit lobortis.</p>
  <div class="btn-more">more...</div>
</article>
<article class="news-card abs" style="left:440px">
  <div class="news-photo" role="img" aria-label="Couple relaxing inside a motorhome while driving" style="background:linear-gradient(135deg,#7a5a3e,#b89a78 45%,#3b78b5 70%,#c9b69a)"></div>
  <div class="news-date">21 Jan 2014</div>
  <p class="news-text">Wisi enim ad minim veniam, quis nostrud exerci tation ullamcorper suscipit lobortis</p>
  <div class="btn-more">more...</div>
</article>
<article class="news-card abs" style="left:782px">
  <div class="news-photo" role="img" aria-label="Motorhome beside a fjord with snowy mountains" style="background:linear-gradient(180deg,#8fb0d0,#dfe6ec 35%,#4b5a52 60%,#2d3b3d)"></div>
  <div class="news-date">25 Jan 2014</div>
  <p class="news-text">Ser wisi enim ad minim veniam, quis nostrud exerci tation ullamcorper suscipit</p>
  <div class="btn-more">more...</div>
</article>

<div class="divider abs"></div>

<div class="deals-head abs">
  <h3>Today's Top Deals</h3>
  <p>Start your search with a look at the best rates on our site.</p>
</div>
<article class="deal abs" style="left:363px">
  <div class="deal-photo" role="img" aria-label="Triumphal arch lit at dusk" style="background:linear-gradient(180deg,#1b3f86,#3f6db0 50%,#b88a4a 85%,#6b4a2a)"></div>
  <div class="deal-name">Paris To Switzerland Delight</div>
  <div class="deal-sub">8-Day Tour From Paris To Switzerland</div>
</article>
<article class="deal abs" style="left:621px">
  <div class="deal-photo" role="img" aria-label="Domed historic building at night" style="background:linear-gradient(180deg,#0e2d6e,#2a4f95 45%,#c9a36a 75%,#4a3a2a)"></div>
  <div class="deal-name">Paris Shopping Bonanza</div>
  <div class="deal-sub">4-Day Paris shop till you drop tour...</div>
</article>
<article class="deal abs" style="left:880px">
  <div class="deal-photo" role="img" aria-label="Canal city waterfront at twilight" style="background:linear-gradient(180deg,#5a7fb2,#c9a36a 45%,#8a5a3a 65%,#2d4a6a)"></div>
  <div class="deal-name">Best of Italy</div>
  <div class="deal-sub">7-Day Tour of Venice, Florence &amp; Rom...</div>
</article>
<div class="deal-nav abs" style="left:363px"><svg width="10" height="14" viewBox="0 0 10 14"><path d="M8 1 L2 7 L8 13" fill="none" stroke="#fff" stroke-width="2"/></svg></div>
<div class="deal-nav abs" style="left:1072px"><svg width="10" height="14" viewBox="0 0 10 14"><path d="M2 1 L8 7 L2 13" fill="none" stroke="#fff" stroke-width="2"/></svg></div>

<footer class="site-footer abs"></footer>
<div class="abs" style="left:100px;top:2164px">
  <div class="foot-title">Follow Us on Social Media</div>
  <div class="social"><span style="background:#3b5998"></span><span style="background:#2aa3dd"></span><span style="background:#d64a3a"></span><span style="background:#c4302b"></span></div>
</div>
<div class="avatar abs" role="img" aria-label="Portrait of a smiling customer"></div>
<div class="testimonial abs">
  <div class="foot-title">Happy Customers</div>
  <p>One thing we never expect when traveling is smooth sailing, but that is exactly what we got! The team of travel coordinators made sure every place we went was accessible and if something wasn't right, they always had a back-up plan. What an amazing vacation!</p>
  <p class="by">- Omar Lindqvist</p>
</div>
<div class="newsletter abs">
  <div class="foot-title">Deals in your Inbox</div>
  <div class="field">First Name</div>
  <div class="field">Last Name</div>
  <div class="field">Enter Email<span class="go"><svg width="10" height="10" viewBox="0 0 10 10"><path d="M1 5 H8 M5 2 L8 5 L5 8" fill="none" stroke="#fff" stroke-width="1.6"/></svg></span></div>
</div>
<div class="support abs">
  <h4>Customer Support</h4>
  <div class="phone">222-333-908</div>
</div>

<div class="bottom-bar abs">
  <span class="copy">Copyright © 2014 - All Rights Reserved</span>
  <nav class="foot-nav">
    <a href="#">Home</a><a href="#">Travel Tours</a><a href="#">About Us</a><a href="#">Blog</a><a href="#">Contact Us</a><a href="#">Terms of Use</a>
  </nav>
</div>

</body>
</html>
```